Business cards for a naturopathic day clinic for stem cell therapy

We need a basic design for a day clinic, that offers stem cell therapies for Lyme therapy and other severe chronic illnesses.
Our name is "Casa velorìn", which can be translated into "Manor Velorbloom". We are a couple of naturopaths working along side physiotherapists and osteopaths, yoga teachers and massage therapists. I attached our logo.

```html
<!DOCTYPE html>
<html lang="en">
<head>
<meta charset="utf-8">
<title>Casa velorìn – business card options</title>
<link rel="stylesheet" href="https://fonts.googleapis.com/css2?family=Questrial&display=swap">
<style>
  :root {
    --green: #b8c762;
    --brown: #8e7d6f;
    --paper: #f2f2f2;
    --faint: #e4e4e4;
    --label: #b3b3b3;
    --white: #ffffff;
  }
  * { margin: 0; padding: 0; box-sizing: border-box; }
  html, body { width: 1200px; height: 1200px; overflow: hidden; background: var(--white); }
  body { position: relative; font-family: "Questrial", "Century Gothic", sans-serif; }

  .option-number {
    position: absolute; top: 106px; width: 80px; margin-left: -40px;
    text-align: center; font-size: 46px; color: var(--label); line-height: 1;
  }

  .card { position: absolute; width: 250px; height: 401px; overflow: hidden; }
  .card--square { left: 148px; }
  .card--rounded { left: 505px; border-radius: 28px; }
  .card--oval { left: 849px; width: 234px; height: 406px; border-radius: 50%; }
  .card--front { top: 230px; }
  .card--back { top: 667px; }
  .card--oval.card--back { top: 671px; }
  .card--paper { background: var(--paper); }
  .card--green { background: var(--green); }

  .front-mark {
    position: absolute; left: 50%; border-radius: 50%; transform: translate(-50%, -50%);
  }
  .front-mark--brown { width: 88px; height: 88px; background: var(--brown); top: 124px; }
  .front-mark--faint { width: 140px; height: 140px; background: var(--faint); top: 178px; }
  .front-mark--white { width: 84px; height: 84px; border: 3px solid var(--white); top: 155px; }

  .front-name {
    position: absolute; left: 0; right: 0; text-align: center;
    font-size: 29px; line-height: 1; white-space: nowrap;
  }
  .front-name--green { color: var(--green); top: 344px; }
  .front-name--white { color: var(--white); top: 282px; font-size: 27px; }

  .back-head { position: absolute; display: flex; align-items: center; gap: 10px; }
  .back-head__dot { width: 28px; height: 28px; border-radius: 50%; flex: none; }
  .back-head__name { font-size: 25px; line-height: 1; white-space: nowrap; }
  .back-head--light .back-head__dot { background: var(--white); }
  .back-head--light .back-head__name { color: var(--white); }
  .back-head--dark .back-head__dot { background: var(--brown); }
  .back-head--dark .back-head__name { color: var(--green); }

  .contact { position: absolute; font-size: 9.5px; line-height: 11.3px; }
  .contact strong { font-weight: 700; }
  .contact--light { color: var(--white); }
  .contact--dark { color: var(--brown); }

  .icon { position: absolute; width: 14px; height: 14px; fill: none; stroke: var(--white); stroke-width: 1.2; }
  .bullet { position: absolute; background: var(--white); border-radius: 3px; }
  .bullet--bar { width: 14px; height: 4px; }
  .bullet--stem { width: 4px; height: 14px; }
  .bullet--green { background: var(--green); width: 14px; height: 4px; }
</style>
</head>
<body>

  <div class="option-number" style="left:269px">1</div>
  <div class="option-number" style="left:627px">2</div>
  <div class="option-number" style="left:967px">3</div>

  <!-- Option 1 -->
  <section class="card card--square card--front card--paper">
    <div class="front-mark front-mark--brown"></div>
    <p class="front-name front-name--green">Casa velorìn</p>
  </section>
  <section class="card card--square card--back card--green">
    <div class="back-head back-head--light" style="left:29px;top:57px">
      <span class="back-head__dot"></span><span class="back-head__name">Casa velorìn</span>
    </div>
    <svg class="icon" style="left:31px;top:154px" viewBox="0 0 14 14"><path d="M1 7 7 1.5 13 7M3 6v6.5h3v-4h2v4h3V6"/></svg>
    <span class="bullet bullet--bar" style="left:31px;top:172px"></span>
    <p class="contact contact--light" style="left:32px;top:185px">Jonas Reller<br>Lindenweg 8<br>64900 Almental<br>Germany</p>
    <svg class="icon" style="left:31px;top:243px" viewBox="0 0 14 14"><path d="M3 1.5 5 4 4 5.5c1 2 2.5 3.5 4.5 4.5L10 9l2.5 2-1.5 1.8C6 12 2 8 1.3 3Z"/></svg>
    <span class="bullet bullet--bar" style="left:31px;top:261px"></span>
    <p class="contact contact--light" style="left:32px;top:274px">+49 6100 5550142<br>06100 5550187</p>
    <svg class="icon" style="left:31px;top:304px" viewBox="0 0 14 14"><circle cx="7" cy="7" r="5.8"/><ellipse cx="7" cy="7" rx="2.6" ry="5.8"/><path d="M1.2 7h11.6M2 4h10M2 10h10"/></svg>
    <span class="bullet bullet--bar" style="left:31px;top:321px"></span>
    <p class="contact contact--light" style="left:32px;top:334px">info@<strong>casa-velorin</strong>.de<br>www.<strong>casa-velorin</strong>.de</p>
  </section>

  <!-- Option 2 -->
  <section class="card card--rounded card--front card--paper">
    <div class="front-mark front-mark--faint"></div>
    <p class="front-name front-name--green">Casa velorìn</p>
  </section>
  <section class="card card--rounded card--back card--green">
    <div class="back-head back-head--light" style="left:29px;top:61px">
      <span class="back-head__dot"></span><span class="back-head__name">Casa velorìn</span>
    </div>
    <svg class="icon" style="left:30px;top:172px" viewBox="0 0 14 14"><path d="M1 7 7 1.5 13 7M3 6v6.5h3v-4h2v4h3V6"/></svg>
    <span class="bullet bullet--stem" style="left:55px;top:172px"></span>
    <p class="contact contact--light" style="left:68px;top:169px">Jonas Reller<br>Lindenweg 8<br>64900 Almental<br>Germany</p>
    <svg class="icon" style="left:30px;top:246px" viewBox="0 0 14 14"><path d="M3 1.5 5 4 4 5.5c1 2 2.5 3.5 4.5 4.5L10 9l2.5 2-1.5 1.8C6 12 2 8 1.3 3Z"/></svg>
    <span class="bullet bullet--stem" style="left:55px;top:246px"></span>
    <p class="contact contact--light" style="left:68px;top:243px">+49 6100 5550142<br>06100 5550187</p>
    <svg class="icon" style="left:30px;top:299px" viewBox="0 0 14 14"><circle cx="7" cy="7" r="5.8"/><ellipse cx="7" cy="7" rx="2.6" ry="5.8"/><path d="M1.2 7h11.6M2 4h10M2 10h10"/></svg>
    <span class="bullet bullet--stem" style="left:55px;top:299px"></span>
    <p class="contact contact--light" style="left:68px;top:296px">info@<strong>casa-velorin</strong>.de<br>www.<strong>casa-velorin</strong>.de</p>
  </section>

  <!-- Option 3 -->
  <section class="card card--oval card--front card--green">
    <div class="front-mark front-mark--white"></div>
    <p class="front-name front-name--white">Casa velorìn</p>
  </section>
  <section class="card card--oval card--back card--paper">
    <div class="back-head back-head--dark" style="left:31px;top:124px">
      <span class="back-head__dot"></span><span class="back-head__name">Casa velorìn</span>
    </div>
    <span class="bullet bullet--green" style="left:48px;top:203px"></span>
    <p class="contact contact--dark" style="left:70px;top:200px">Jonas Reller<br>Lindenweg 8<br>64900 Almental<br>Germany</p>
    <span class="bullet bullet--green" style="left:48px;top:266px"></span>
    <p class="contact contact--dark" style="left:70px;top:263px">+49 6100 5550142<br>06100 5550187</p>
    <span class="bullet bullet--green" style="left:48px;top:302px"></span>
    <p class="contact contact--dark" style="left:70px;top:299px">info@<strong>casa-velorin</strong>.de<br>www.<strong>casa-velorin</strong>.de</p>
  </section>

</body>
</html>
```